Business card design

Hi,
I need to have a business card design based on the current logo.
If competitive I not put it out to everyone.

It can be single of double sided

Target Market(s)

Food businesses

Industry/Entity Type

Food Manufacturing

Contact Information for Business Card

Details will on card will be as follows Name = Marcus Pell Email = Marcus@BrimKitchens.com.au Phone = 0418562307 Address = 57 Tallowmere Road , Fortitude Valley QLD 4006 Australia

Font styles to use
Other font styles liked:
• based on two fonts - Adelle & Museo

Requirements
Must have
• Based on the on switch concept

```html
<!DOCTYPE html>
<html lang="en">
<head>
<meta charset="utf-8">
<title>BrimKitchens Business Card</title>
<link rel="stylesheet" href="https://fonts.googleapis.com/css2?family=Montserrat:wght@500;600;700&family=Zilla+Slab:wght@500&display=swap">
<style>
  :root {
    --page-bg: #9b9b9b;
    --card-white: #ffffff;
    --card-dark: #372024;
    --brand-red: #ee2a47;
    --ink: #372024;
    --ink-soft: #4a4446;
  }
  * { margin: 0; padding: 0; box-sizing: border-box; }
  html, body { width: 1133px; height: 1200px; overflow: hidden; }
  body {
    background: var(--page-bg);
    position: relative;
    font-family: "Montserrat", Arial, sans-serif;
  }
  .card {
    position: absolute;
    left: 205px;
    width: 724px;
    height: 414px;
    border-radius: 26px;
    overflow: hidden;
  }
  .card--front { top: 140px; background: var(--card-white); }
  .card--back { top: 645px; background: var(--card-dark); }

  .brand {
    position: absolute;
    left: 61px;
    top: 67px;
    display: flex;
    align-items: center;
    gap: 12px;
  }
  .brand__dot {
    width: 40px; height: 40px;
    border-radius: 50%;
    background: var(--brand-red);
  }
  .brand__name {
    font-weight: 600;
    font-size: 36px;
    letter-spacing: 0.5px;
    color: var(--ink);
    line-height: 1;
  }
  .tagline {
    position: absolute;
    left: 61px;
    width: 311px;
    top: 114px;
    text-align: right;
    font-family: "Zilla Slab", Georgia, serif;
    font-weight: 500;
    font-size: 14px;
    color: var(--ink);
  }
  .holder-name {
    position: absolute;
    left: 61px;
    top: 270px;
    font-weight: 700;
    font-size: 26px;
    letter-spacing: 0.6px;
    color: var(--brand-red);
  }
  .contact {
    position: absolute;
    left: 443px;
    top: 211px;
    font-weight: 500;
    font-size: 16.5px;
    line-height: 20.5px;
    color: var(--ink-soft);
  }
  .contact__address { margin-bottom: 14px; }
  .web-rule {
    position: absolute;
    left: 0; right: 0;
    display: flex;
    align-items: center;
  }
  .web-rule::before, .web-rule::after {
    content: "";
    flex: 1;
    height: 2px;
    background: var(--ink);
  }
  .web-rule--front { top: 352px; }
  .web-rule--front::before { flex: 0 0 432px; }
  .web-rule__text {
    padding: 0 12px;
    font-weight: 500;
    font-size: 17px;
    color: var(--ink);
    white-space: nowrap;
  }
  .back-brand {
    position: absolute;
    left: 0; right: 0;
    top: 180px;
    display: flex;
    justify-content: center;
    align-items: center;
    gap: 16px;
  }
  .back-brand__dot {
    width: 56px; height: 56px;
    border-radius: 50%;
    background: var(--brand-red);
  }
  .back-brand__name {
    font-weight: 600;
    font-size: 44px;
    color: var(--card-white);
    letter-spacing: 0.5px;
  }
  .web-rule--back { top: 356px; }
  .web-rule--back::before, .web-rule--back::after { height: 2px; background: var(--brand-red); }
  .web-rule--back::before { flex: 0 0 236px; }
  .web-rule--back .web-rule__text {
    font-size: 15.5px;
    letter-spacing: 3.5px;
    color: var(--card-white);
  }
  .web-rule__highlight { color: var(--brand-red); }
</style>
</head>
<body>
  <section class="card card--front">
    <div class="brand">
      <span class="brand__dot"></span>
      <span class="brand__name">BRIMKITCHENS</span>
    </div>
    <p class="tagline">Kitchen Support On Call</p>
    <h1 class="holder-name">MARCUS PELL</h1>
    <div class="contact">
      <p class="contact__address">57 Tallowmere Road<br>Marrowvale<br>QLD 4012 Australia</p>
      <p>Ph. 041-856-2307<br>Marcus@BrimKitchens.com.au</p>
    </div>
    <div class="web-rule web-rule--front">
      <span class="web-rule__text">www.BrimKitchens.com.au</span>
    </div>
  </section>

  <section class="card card--back">
    <div class="back-brand">
      <span class="back-brand__dot"></span>
      <span class="back-brand__name">BRIMKITCHENS</span>
    </div>
    <div class="web-rule web-rule--back">
      <span class="web-rule__text">www.<span class="web-rule__highlight">BrimKitchens</span>.com.au</span>
    </div>
  </section>
</body>
</html>
```